product development company BRVENKO LLC business card

We need a business card design for a company based in Texas called 'BRVENKO LLC'. Our first product is a illuminated portable ice chest that is called ' Pebble Drift coolers'. Pebble drift coolers is trademarked. I would like to have the pebble drift trademark somewhere on the card as well as the BRVENKO LLC name.

Target Market(s)

outdoor industry

Industry/Entity Type

Business

Contact Information for Business Card

i would like to have BRVENKO LLC logo larger than the Pebble drift coolers logo.

Font styles to use
Serif
Sans Serif

```html
<!DOCTYPE html>
<html lang="en">
<head>
<meta charset="utf-8">
<title>BRVENKO LLC business card</title>
<link rel="stylesheet" href="https://fonts.googleapis.com/css2?family=Cinzel:wght@600;700&family=Tinos:wght@400;700&display=swap">
<style>
  :root {
    --stage: #2b2b2b;
    --card-dark: #1e1b1c;
    --card-dark-mark: #242122;
    --card-light: #ffffff;
    --mark-light: #e6e6e8;
    --ink: #111111;
    --ink-soft: #7a7a7a;
    --paper-text: #f4f4f4;
    --icon: #9a9a9a;
  }
  html, body {
    margin: 0;
    padding: 0;
    width: 1189px;
    height: 1200px;
    overflow: hidden;
    background: var(--stage);
  }
  .card {
    position: absolute;
    left: 172px;
    width: 855px;
    height: 487px;
    overflow: hidden;
  }
  .card--front { top: 68px; background: var(--card-dark); }
  .card--back  { top: 627px; background: var(--card-light); }

  .bg-mark { position: absolute; inset: 0; }

  .brand {
    position: absolute;
    font-family: "Cinzel", serif;
    font-weight: 700;
    text-align: center;
  }
  .brand__name {
    display: block;
    letter-spacing: 6px;
    line-height: 1;
  }
  .brand__suffix {
    display: flex;
    align-items: center;
    justify-content: center;
    gap: 16px;
    font-weight: 600;
    letter-spacing: 12px;
    line-height: 1;
  }
  .brand__dots {
    display: inline-block;
    border-bottom: 3px dotted currentColor;
    width: 96px;
    height: 0;
    transform: translateY(-4px);
  }

  .card--front .brand {
    left: 0; right: 0; top: 182px;
    color: var(--paper-text);
  }
  .card--front .brand__name { font-size: 74px; }
  .card--front .brand__suffix { font-size: 36px; margin-top: 14px; }

  .card--back .brand {
    left: 40px; top: 54px;
    color: var(--ink);
  }
  .card--back .brand__name { font-size: 58px; }
  .card--back .brand__suffix { font-size: 30px; margin-top: 10px; }
  .card--back .brand__dots { width: 74px; }

  .contact {
    position: absolute;
    left: 43px;
    font-family: "Tinos", serif;
    color: var(--ink);
  }
  .person { top: 218px; }
  .person__name { font-size: 25px; font-weight: 700; line-height: 1; margin: 0; }
  .person__role { font-size: 19px; color: var(--ink-soft); line-height: 1.1; margin: 0; }

  .address { top: 296px; font-size: 21px; line-height: 29px; margin: 0; }

  .lines { top: 372px; list-style: none; margin: 0; padding: 0; font-size: 21px; }
  .lines li { display: flex; align-items: center; gap: 8px; height: 27px; }
  .lines svg { width: 22px; height: 22px; flex: none; }

  .product {
    position: absolute;
    left: 596px;
    top: 372px;
    font-family: "Tinos", serif;
    font-weight: 700;
    color: var(--ink);
    text-align: right;
  }
  .product__row { display: flex; align-items: center; gap: 8px; }
  .product__dot { width: 22px; height: 22px; border-radius: 50%; background: var(--ink); }
  .product__name { font-size: 30px; line-height: 1; }
  .product__line { font-size: 12px; letter-spacing: 4px; margin-top: 6px; }
</style>
</head>
<body>

<section class="card card--front">
  <svg class="bg-mark" viewBox="0 0 855 487" aria-hidden="true">
    <circle cx="600" cy="300" r="250" fill="var(--card-dark-mark)"/>
  </svg>
  <div class="brand">
    <span class="brand__name">BRVENKO</span>
    <span class="brand__suffix"><i class="brand__dots"></i>LLC<i class="brand__dots"></i></span>
  </div>
</section>

<section class="card card--back">
  <svg class="bg-mark" viewBox="0 0 855 487" aria-hidden="true">
    <circle cx="640" cy="250" r="230" fill="var(--mark-light)"/>
  </svg>

  <div class="brand">
    <span class="brand__name">BRVENKO</span>
    <span class="brand__suffix"><i class="brand__dots"></i>LLC<i class="brand__dots"></i></span>
  </div>

  <div class="contact person">
    <p class="person__name">DALE MORROW</p>
    <p class="person__role">Maneger</p>
  </div>

  <p class="contact address">Your Address,2nd Ste<br>Larkvale, Westmoor 1234</p>

  <ul class="contact lines">
    <li>
      <svg viewBox="0 0 22 22" aria-hidden="true"><rect width="22" height="22" fill="var(--icon)"/><path d="M6 5c1-1 2 0 3 2s0 2-1 3c1 2 2 3 4 4 1-1 1-2 3-1s3 2 2 3c-2 3-6 1-9-2S3 8 6 5z" fill="#fff"/></svg>
      123 456 7890
    </li>
    <li>
      <svg viewBox="0 0 22 22" aria-hidden="true"><rect width="22" height="22" fill="var(--icon)"/><rect x="4" y="6" width="14" height="10" fill="none" stroke="#fff" stroke-width="1.5"/><path d="M4 6l7 6 7-6" fill="none" stroke="#fff" stroke-width="1.5"/></svg>
      your@yourcompany.com
    </li>
    <li>
      <svg viewBox="0 0 22 22" aria-hidden="true"><rect width="22" height="22" fill="var(--icon)"/><circle cx="11" cy="11" r="7" fill="none" stroke="#fff" stroke-width="1.3"/><ellipse cx="11" cy="11" rx="3" ry="7" fill="none" stroke="#fff" stroke-width="1.1"/><path d="M4 11h14M5 7.5h12M5 14.5h12" stroke="#fff" stroke-width="1"/></svg>
      www.yourcompany.com
    </li>
  </ul>

  <div class="product">
    <div class="product__row">
      <span class="product__dot"></span>
      <span class="product__name">Pebble Drift</span>
    </div>
    <div class="product__line">COOLERS</div>
  </div>
</section>

</body>
</html>
```